A new PowerPoint Template for a French consulting company

Who are we?

Formed in 2005, Quorv is a consulting company specialising in the human aspect of change and transformation.

From our offices in the heart of Paris, our team of 30 consultants work with leading organisations in the Aerospace, Finance, Transportation and Public sectors to deliver lasting change.

Our customers trust us with some of their most strategic and sensitive projects. They trust us with these projects because:
- We listen to them, ensuring we understand the real needs of their business
- We involve them, co-developing and tailoring our solutions to the specific challenges they face
- We’re professional, without taking ourselves too seriously
- We’re imaginative, whilst always remaining pragmatic
- We get results!

You can find out more about who we are and the work we do here: http://www.quorv-example.fr/en

What we need from you?

We’re approaching our 10th birthday and, whilst we still love what we do, we think it’s the right time to update our image.

We’d like you to design us a new PowerPoint template, that will be used for all of our internal and client facing work. You can base your submissions on our existing logo and colour scheme (see files attached) or you can submit your own fresh ideas – after all, we’re not afraid of change!

Finally, whilst we’re looking for you to be creative, there are some simple guidelines that we need you to keep in mind:

1. The Template needs to include both a front cover and a “content” page

2. The front cover needs to:
- Include our logo
- Reflect “who we are” and the type of work that we do

3. The content page needs to:
- Have a predominantly white background
- Be practical to use, making an effective use of the 4:3 standard PPT size
- Include an area across the top of the page for the slide title
- Include areas along the bottom of the page for the page number and date

4. If you decide to propose a new colour scheme, it should be balanced and the “accents” usable

5. The PowerPoint Template needs to be “printer friendly”

6. The fonts you use should be standard

What we don’t want?

To give you as much help as possible, here are some things that we really don’t want:

- Submissions that are dull grey or navy blue, suggesting we’re nothing but boring corporate suits
- Submissions that are Lulette pink or too “soft and cuddly”
- Submissions that use lots of stock images of “happy, smiling, consultants”
- Submissions that will be the height of fashion today, but completely out of date next year

```html
<!DOCTYPE html>
<html lang="en">
<head>
<meta charset="utf-8">
<title>Quorv — Presentation Template</title>
<link rel="stylesheet" href="https://fonts.googleapis.com/css2?family=Roboto+Condensed:wght@300;400;700&display=swap">
<style>
  :root {
    --teal: #00a096;
    --teal-light: #a8dcdb;
    --plum: #6b1f4c;
    --plum-deep: #5a1641;
    --grey-text: #8f8f8f;
    --grey-dark: #7a7a7a;
    --sheet-white: #ffffff;
    --sheet-grey: #e2e2e2;
    --backdrop-1: #8a8a8a;
    --backdrop-2: #5e5e5e;
  }
  * { margin: 0; padding: 0; box-sizing: border-box; }
  html, body { width: 1200px; height: 1000px; overflow: hidden; }
  body {
    position: relative;
    font-family: "Roboto Condensed", "Arial Narrow", sans-serif;
    background: radial-gradient(ellipse at 50% 40%, var(--backdrop-1), var(--backdrop-2));
  }
  .slide {
    position: absolute;
    width: 528px;
    height: 396px;
    overflow: hidden;
    box-shadow: 2px 3px 6px rgba(0,0,0,.35);
  }
  .slide svg.shapes { position: absolute; inset: 0; width: 528px; height: 396px; }
  .slide--cover { left: 47px; top: 82px;
    background: linear-gradient(90deg, var(--sheet-grey) 45%, var(--sheet-white) 90%); }
  .slide--content { left: 624px; top: 82px;
    background: linear-gradient(180deg, var(--sheet-white) 60%, var(--sheet-grey) 100%); }
  .slide--closing { left: 354px; top: 540px;
    background: linear-gradient(90deg, var(--sheet-grey) 55%, var(--sheet-white) 100%); }

  .brand-name {
    position: absolute;
    color: var(--plum);
    font-weight: 700;
    letter-spacing: -0.5px;
    line-height: 1;
  }
  .slide--cover .brand-name { right: 31px; top: 58px; font-size: 42px; }
  .slide--content .brand-name { right: 99px; top: 27px; font-size: 24px; }
  .slide--closing .brand-name { right: 59px; top: 258px; font-size: 30px; }

  .cover-date {
    position: absolute; right: 31px; top: 200px;
    font-size: 11px; font-weight: 700; color: var(--grey-dark);
  }
  .cover-title {
    position: absolute; right: 31px; top: 213px;
    text-align: right; font-size: 29px; font-weight: 300;
    line-height: 26px; color: var(--grey-text); text-transform: uppercase;
  }
  .footer-tag {
    position: absolute; bottom: 0; height: 20px;
    color: #fff; font-weight: 700; line-height: 20px;
  }
  .slide--cover .footer-tag { right: 0; width: 170px; font-size: 10.5px; padding-left: 22px; }
  .slide--content .footer-tag { left: 0; width: 110px; font-size: 8.5px; padding-left: 16px; }

  .slide-title {
    position: absolute; left: 32px; top: 76px;
    font-size: 28px; font-weight: 300; color: var(--teal);
  }
  .slide-body {
    position: absolute; left: 44px; top: 126px; width: 420px;
    font-size: 11.5px; line-height: 15px; color: var(--grey-text);
  }
  .slide-body p + p { margin-top: 15px; }

  .page-marker {
    position: absolute; right: 18px; bottom: 5px;
    display: flex; align-items: flex-end; gap: 4px;
  }
  .page-marker__section { font-size: 8.5px; color: var(--teal); }
  .page-marker__slash { width: 1px; height: 18px; background: var(--grey-text); transform: skewX(-20deg) rotate(20deg); }
  .page-marker__number { font-size: 12px; font-weight: 700; color: var(--plum); }

  .closing-message {
    position: absolute; left: 0; top: 86px; width: 324px;
    text-align: center; font-size: 54px; font-weight: 300;
    line-height: 50px; color: #fff;
  }
  .contact-block {
    position: absolute; right: 59px; top: 300px;
    text-align: right; font-size: 10px; font-weight: 700;
    line-height: 13px; color: var(--grey-dark);
  }
</style>
</head>
<body>

  <!-- Cover slide -->
  <section class="slide slide--cover">
    <svg class="shapes" viewBox="0 0 528 396" aria-hidden="true">
      <polygon points="0,28 310,28 187,396 0,396" fill="var(--teal-light)"/>
      <polygon points="0,0 238,0 128,328 0,328" fill="var(--teal)"/>
      <polygon points="157,152 224,152 152,370 84,370" fill="var(--plum)" opacity="0.9"/>
      <polygon points="443,0 480,0 467,33 431,33" fill="var(--teal)"/>
      <polygon points="378,376 528,376 528,396 371,396" fill="var(--plum)"/>
    </svg>
    <div class="brand-name">Quorv</div>
    <div class="cover-date">SEPTEMBER 14, 2014</div>
    <h1 class="cover-title">Presentation<br>Title</h1>
    <div class="footer-tag">WWW.QUORV-EXAMPLE.FR</div>
  </section>

  <!-- Content slide -->
  <section class="slide slide--content">
    <svg class="shapes" viewBox="0 0 528 396" aria-hidden="true">
      <polygon points="461,0 487,0 464,71 438,71" fill="var(--teal)"/>
      <polygon points="490,0 501,0 479,71 467,71" fill="var(--teal-light)"/>
      <polygon points="0,376 106,376 99,396 0,396" fill="var(--plum)"/>
    </svg>
    <div class="brand-name">Quorv</div>
    <h2 class="slide-title">ABOUT US</h2>
    <div class="slide-body">
      <p>Quorv, a consulting firm specializing in change management, helps major organizations to design and implement their transformation programs.</p>
      <p>Quorv has developed quickly since its creation in 2005, due to major and continuing private and public clients in industrial and service sectors.</p>
      <p>Quorv works mainly in Europe.</p>
      <p>Quorv offers all the different steps of a transformation program, from conception to implementation.</p>
      <p>Shared by all consultants, these convictions are the primary success factors in Quorv’s interventions.</p>
    </div>
    <div class="footer-tag">SEPTEMBER 14, 2014</div>
    <div class="page-marker">
      <span class="page-marker__section">ABOUT US</span>
      <span class="page-marker__slash"></span>
      <span class="page-marker__number">2</span>
    </div>
  </section>

  <!-- Closing slide -->
  <section class="slide slide--closing">
    <svg class="shapes" viewBox="0 0 528 396" aria-hidden="true">
      <polygon points="0,0 373,0 306,247 0,247" fill="var(--teal)"/>
      <polygon points="373,0 424,0 378,140 326,140" fill="var(--plum)" opacity="0.8"/>
      <polygon points="0,247 306,247 262,396 0,396" fill="var(--teal-light)"/>
      <polygon points="266,280 294,280 258,396 213,396" fill="var(--teal)"/>
      <polygon points="246,247 274,247 254,315 226,315" fill="var(--plum)" opacity="0.8"/>
      <polygon points="0,295 104,295 74,396 0,396" fill="var(--plum)"/>
    </svg>
    <div class="closing-message">THANK<br>YOU!</div>
    <div class="brand-name">Quorv</div>
    <address class="contact-block" style="font-style:normal">
      24 rue Vernal<br>
      75009 Paris - France<br>
      +33 (0) 1 55 42 19 30<br>
      www.quorv-example.fr
    </address>
  </section>

</body>
</html>
```